Executive Performance Review mapped on J-curve

I need to turn an executive company performance review into a visual infographic. The list of accomplishments is grouped into four calendar quarters. Each quarter needs a subtle representation of the season. The four quarters and associated list of accomplishments need to be mapped to a J-curve. - Spreadsheet with accomplishments attached (Throughput)- Sample image of a J-curve. You can google J-curve to see more images.- The title should be "Dorna Pelsketh Year in Review"

Target Market(s)

Board of Directors

Requirements
Nice to have
• This will be presented to a company founder that is an artist and customer experience expert. He is very visual so a nice visual representation of the data will be impactful. He also uses the phrase that you have to live with or work with someone for four seasons before you really know them. This is why I have the seasons mapped to the quarters. The Fall season motif should be gloomy and stormy.

```html
<!DOCTYPE html>
<html lang="en">
<head>
<meta charset="utf-8">
<title>Dorna Pelsketh Year in Review</title>
<link rel="stylesheet" href="https://fonts.googleapis.com/css2?family=Oswald:wght@400;500;600&family=Open+Sans:wght@400;600&family=Raleway:wght@300&display=swap">
<style>
  :root{
    --summer:#f2cf4a;
    --summer-text:#e4b52a;
    --fall:#a8a8aa;
    --fall-dark:#8e8e90;
    --winter:#29a8df;
    --spring:#f4868a;
    --ink:#5b5b5e;
    --frame:#cfcfd1;
    --paper:#f8f8f8;
  }
  *{box-sizing:border-box;margin:0;padding:0}
  html,body{width:1041px;height:1200px;overflow:hidden;background:var(--paper)}
  .canvas{position:relative;width:1041px;height:1200px;overflow:hidden;
    background:radial-gradient(circle at 50% 50%,#ffffff 0,#f9f9f9 40%,#f5f5f5 100%);
    font-family:"Open Sans",sans-serif;color:var(--ink)}
  .artwork{position:absolute;left:0;top:0;width:1041px;height:1200px}
  .artwork .heading-name{font-family:"Raleway",sans-serif;font-weight:300;font-size:40px;fill:#555}
  .artwork .heading-title{font-family:"Oswald",sans-serif;font-weight:600;font-size:96px;fill:#77777a}
  .artwork .season{font-family:"Oswald",sans-serif;font-weight:400;font-size:30px}
  .artwork .quarter{font-family:"Oswald",sans-serif;font-weight:600;font-size:50px}
  .artwork .goal-year{font-family:"Oswald",sans-serif;font-weight:600;font-size:68px;fill:var(--spring)}
  .artwork .goal-name{font-family:"Oswald",sans-serif;font-weight:400;font-size:42px;fill:var(--spring)}
  .artwork .phase-label{font-family:"Oswald",sans-serif;font-weight:500;font-size:36px;fill:#fff}

  .column{position:absolute;top:762px;width:220px;font-size:9.6px;line-height:12.4px}
  .col-assessment{left:86px;--accent:var(--summer)}
  .col-stabilize{left:310px;--accent:var(--fall)}
  .col-stratactical{left:533px;--accent:var(--winter)}
  .col-strategic{left:757px;--accent:var(--spring)}
  .section-title{font-weight:600}
  .col-assessment .section-title{color:var(--summer-text)}
  .col-stabilize .section-title{color:var(--ink)}
  .col-stratactical .section-title{color:var(--winter)}
  .col-strategic .section-title{color:var(--spring)}
  .section + .section{margin-top:12.4px}
  .group{list-style:none}
  .group > li{position:relative;padding-left:14.5px}
  .group > li::before{content:"";position:absolute;left:3.5px;top:3px;border-left:6px solid var(--accent);border-top:3.5px solid transparent;border-bottom:3.5px solid transparent}
  .items{list-style:none}
  .items li{position:relative;padding-left:29px;text-indent:-14.5px}
  .items li::before{content:"";position:absolute;left:5px;top:2.5px;width:3px;height:6px;border-right:1.6px solid var(--accent);border-bottom:1.6px solid var(--accent);transform:rotate(45deg)}
</style>
</head>
<body>
<div class="canvas">
  <svg class="artwork" viewBox="0 0 1792 2065" aria-label="J-curve timeline from Q3 2018 to 2020">
    <path d="M465 115 H60 V2017 H1725 V115 H1297" fill="none" stroke="var(--frame)" stroke-width="3"/>
    <circle cx="323" cy="115" r="15" fill="#d6d6d8"/>
    <circle cx="394" cy="115" r="19" fill="#a2a2a5"/>
    <circle cx="465" cy="115" r="24" fill="var(--spring)"/>
    <circle cx="1297" cy="112" r="24" fill="var(--spring)"/>
    <circle cx="1368" cy="112" r="19" fill="#a2a2a5"/>
    <circle cx="1439" cy="112" r="15" fill="#d6d6d8"/>

    <text class="heading-name" x="642" y="84" textLength="498" lengthAdjust="spacing">DORNA PELSKETH</text>
    <text class="heading-title" x="590" y="183" textLength="605" lengthAdjust="spacingAndGlyphs">YEAR IN REVIEW</text>

    <g fill="none" stroke-width="30" stroke-linecap="round">
      <path d="M530 778 C555 870 610 915 690 918" stroke="var(--summer)"/>
      <path d="M690 918 C790 900 880 840 947 771" stroke="var(--fall)"/>
      <path d="M947 771 L1120 569" stroke="var(--winter)"/>
      <path d="M1120 569 L1260 402" stroke="var(--spring)"/>
    </g>

    <circle cx="530" cy="778" r="24" fill="var(--summer)"/><circle cx="530" cy="778" r="10" fill="#fff"/>
    <circle cx="690" cy="918" r="24" fill="var(--fall)"/><circle cx="690" cy="918" r="10" fill="#fff"/>
    <circle cx="947" cy="771" r="24" fill="var(--winter)"/><circle cx="947" cy="771" r="10" fill="#fff"/>
    <circle cx="1120" cy="569" r="24" fill="var(--spring)"/><circle cx="1120" cy="569" r="10" fill="#fff"/>
    <circle cx="1283" cy="373" r="48" fill="var(--spring)"/>
    <circle cx="1283" cy="373" r="32" fill="#fff"/>
    <circle cx="1283" cy="373" r="20" fill="var(--spring)"/>
    <circle cx="1283" cy="373" r="9" fill="#fff"/>

    <g stroke="var(--summer)" stroke-width="3" fill="none">
      <path d="M574 778 A44 44 0 0 0 530 734 A44 44 0 0 0 487 770 V777 H256"/>
    </g>
    <circle cx="256" cy="777" r="9" fill="var(--summer)"/>
    <g fill="var(--summer)">
      <circle cx="205" cy="773" r="22"/>
      <g stroke="var(--summer)" stroke-width="6" stroke-linecap="round">
        <path d="M205 743v-6M205 803v6M175 773h-6M235 773h6M184 752l-4-4M226 794l4 4M226 752l4-4M184 794l-4 4"/>
      </g>
    </g>
    <circle cx="205" cy="773" r="15" fill="none" stroke="#fff" stroke-width="2"/>
    <text class="season" x="297" y="763" fill="var(--summer-text)">SUMMER</text>
    <text class="quarter" x="297" y="830" fill="var(--summer-text)">Q3 2018</text>

    <g stroke="var(--fall)" stroke-width="3" fill="none">
      <path d="M655 942 A40 40 0 0 0 727 942"/>
      <path d="M690 966 V1012 Q690 1027 675 1027 H440"/>
    </g>
    <circle cx="440" cy="1027" r="9" fill="var(--fall)"/>
    <g fill="var(--fall-dark)">
      <path d="M390 998 L398 1012 L414 1006 L408 1022 L420 1030 L400 1034 L392 1044 L386 1034 L364 1030 L376 1022 L370 1006 L384 1012 Z"/>
      <path d="M390 1030 L392 1060" stroke="var(--fall-dark)" stroke-width="3"/>
    </g>
    <text class="season" x="477" y="1011" fill="var(--fall)">FALL</text>
    <text class="quarter" x="477" y="1073" fill="var(--fall)">Q4 2018</text>

    <g stroke="var(--winter)" stroke-width="3" fill="none">
      <path d="M988 762 A42 42 0 0 1 937 814"/>
      <path d="M980 805 Q1010 845 1040 846 H1257"/>
    </g>
    <circle cx="1257" cy="846" r="9" fill="var(--winter)"/>
    <g stroke="var(--winter)" stroke-width="5" stroke-linecap="round">
      <path d="M1303 816V876M1277 831L1329 861M1277 861L1329 831"/>
      <path d="M1295 822l8 6 8-6M1295 870l8-6 8 6"/>
    </g>
    <circle cx="1303" cy="846" r="7" fill="var(--winter)"/>
    <text class="season" x="1055" y="830" fill="var(--winter)">WINTER</text>
    <text class="quarter" x="1055" y="898" fill="var(--winter)">Q1 2019</text>

    <g stroke="var(--spring)" stroke-width="3" fill="none">
      <path d="M1162 560 A42 42 0 0 1 1112 610"/>
      <path d="M1155 600 Q1190 640 1215 641 H1432"/>
    </g>
    <circle cx="1432" cy="641" r="9" fill="var(--spring)"/>
    <g fill="var(--spring)">
      <circle cx="1480" cy="622" r="12"/><circle cx="1498" cy="635" r="12"/>
      <circle cx="1492" cy="657" r="12"/><circle cx="1468" cy="657" r="12"/>
      <circle cx="1462" cy="635" r="12"/>
    </g>
    <circle cx="1480" cy="641" r="8" fill="#fff"/>
    <text class="season" x="1226" y="621" fill="var(--spring)">SPRING</text>
    <text class="quarter" x="1226" y="688" fill="var(--spring)">Q2 2019</text>

    <text class="goal-year" x="1358" y="364">2020</text>
    <text class="goal-name" x="1358" y="414">VALUE CREATION</text>

    <path d="M145 1245 H1640" stroke="#9c9c9e" stroke-width="2.5" stroke-dasharray="3 9"/>
    <circle cx="145" cy="1246" r="8" fill="var(--summer)"/>
    <circle cx="1640" cy="1245" r="8" fill="var(--spring)"/>

    <rect x="228" y="1218" width="254" height="54" rx="27" fill="var(--summer)"/>
    <circle cx="263" cy="1245" r="13" fill="none" stroke="#fff" stroke-width="3"/>
    <text class="phase-label" x="299" y="1258" textLength="151" lengthAdjust="spacingAndGlyphs">ASSESSMENT</text>

    <rect x="616" y="1218" width="214" height="54" rx="27" fill="var(--fall)"/>
    <circle cx="652" cy="1245" r="13" fill="#fff"/>
    <text class="phase-label" x="686" y="1258" textLength="114" lengthAdjust="spacingAndGlyphs">STABILIZE</text>

    <rect x="955" y="1218" width="261" height="54" rx="27" fill="var(--winter)"/>
    <g stroke="#fff" stroke-width="3" stroke-linecap="round"><path d="M994 1228V1262M979 1236L1009 1254M979 1254L1009 1236"/></g>
    <text class="phase-label" x="1026" y="1258" textLength="164" lengthAdjust="spacingAndGlyphs">STRATACTICAL</text>

    <rect x="1343" y="1218" width="222" height="54" rx="27" fill="var(--spring)"/>
    <circle cx="1381" cy="1245" r="14" fill="none" stroke="#fff" stroke-width="3"/>
    <circle cx="1381" cy="1245" r="5" fill="#fff"/>
    <text class="phase-label" x="1414" y="1258" textLength="123" lengthAdjust="spacingAndGlyphs">STRATEGIC</text>
  </svg>

  <div class="column col-assessment">
    <div class="section">
      <div class="section-title">Throughput</div>
      <ul class="group">
        <li>Transitions
          <ul class="items"><li>RO Transition from Rolf &amp; Mira</li><li>Start CR Office Initiative</li><li>Tactical Ops transition from Rolf</li><li>Formalize Exec Team</li></ul></li>
        <li>Biz Architecture
          <ul class="items"><li>Independent Financial Audit</li><li>Organizational Audit - Structure</li><li>Organizational Audit - People</li><li>XF Framework - ESU</li><li>Defined Utilization, Realization, Availability</li></ul></li>
        <li>Strategy
          <ul class="items"><li>Effective Strategy Meeting</li><li>Strategic Themes 2018 - 2020: Stablize, Accelerate, Surge</li><li>Business Drivers: Drive Revenue, Improve Corvane Experience, Increase Brand Awareness</li></ul></li>
        <li>Sales
          <ul class="items"><li>Talmore Account Transition</li><li>QVS Account Transition</li><li>2 year Managed Services Engagement Model</li></ul></li>
        <li>Revenue / EBITA
          <ul class="items"><li>TBD</li></ul></li>
      </ul>
    </div>
    <div class="section">
      <div class="section-title">Effectiveness</div>
      <ul class="group"><li>Storming</li></ul>
    </div>
  </div>

  <div class="column col-stabilize">
    <div class="section">
      <div class="section-title">Throughput</div>
      <ul class="group">
        <li>Biz Architecture
          <ul class="items"><li>XF Framework - Functional Meetings &amp; Scrum of Scrums</li><li>Structured Reorg</li><li>Implemented Reorg</li><li>Quarterly Org Iteration cadence</li><li>Defined Key Hire Plan</li><li>CR Office Operational</li><li>Time Accountability</li><li>Tools ReConfig</li><li>Org Structure v1</li></ul></li>
        <li>Strategy
          <ul class="items"><li>Internal QBR Accountability</li></ul></li>
        <li>Sales
          <ul class="items"><li>Brenwick QBR</li><li>Talmore QBR</li></ul></li>
        <li>Revenue / EBITA
          <ul class="items"><li>TBD</li></ul></li>
      </ul>
    </div>
    <div class="section">
      <div class="section-title">Effectiveness</div>
      <ul class="group"><li>Activity</li></ul>
    </div>
  </div>

  <div class="column col-stratactical">
    <div class="section">
      <div class="section-title">Throughput</div>
      <ul class="group">
        <li>Biz Architecture
          <ul class="items"><li>XF Framework - Progress Demos</li><li>Org Structure - COE's</li><li>Stablize Accounting &amp; Finance</li><li>Exec Hiring Process</li></ul></li>
        <li>Key Hires
          <ul class="items"><li>Controller</li><li>Director CX</li></ul></li>
        <li>Strategy
          <ul class="items"><li>Founders removed from front line activity</li><li>Velmar QBR - Goal Setting &amp; Tracking</li><li>Sales</li><li>QVS QBR</li><li>Talmore QBR</li></ul></li>
        <li>Revenue / EBITA
          <ul class="items"><li>TBD</li></ul></li>
      </ul>
    </div>
    <div class="section">
      <div class="section-title">Effectiveness</div>
      <ul class="group"><li>Throughput</li></ul>
    </div>
  </div>

  <div class="column col-strategic">
    <div class="section">
      <div class="section-title">Throughput</div>
      <ul class="group">
        <li>Biz Architecture
          <ul class="items"><li>Tiered Pricing Pre-Paid Engagement Model</li><li>XF Framework - Ideation Board</li><li>Consulting Levels &amp; Salary Bands</li><li>Roles &amp; Responsibilities</li></ul></li>
        <li>Key Hires
          <ul class="items"><li>Interim HR</li><li>Provisional Client Partner</li><li>Acting Director 1</li><li>Acting Director 2</li><li>Client Partner 1</li><li>Sales Exec 1</li></ul></li>
        <li>Sales
          <ul class="items"><li>Opened Glassline Door</li><li>Flipped focus from operationaly run company to sales/marketing driven org</li><li>KTR Direct</li></ul></li>
        <li>Revenue / EBITA
          <ul class="items"><li>TBD</li></ul></li>
      </ul>
    </div>
    <div class="section">
      <div class="section-title">Effectiveness</div>
      <ul class="group"><li>Outcomes</li></ul>
    </div>
  </div>
</div>
</body>
</html>
```